Bright Tutor Hub business card

Use existing logo to design a business card which contains information that is listed below. Use of logo as attached. It is important that the colour scheme matches the logo already designed. It needs to be crisp and professional. This is an on line business, a database of training providers for educational establishments. The website will provide users with full information on trainers who are available and their credibility.
Target Market(s)
Educators and training providers
Industry/Entity Type
Education
Contact Information for Business Card
Font styles to use
Colors
Designer to choose colors to be used in the design.
Requirements
Must have
- Email address mara@brighttutorhub.co.uk
- Twitter feed. @MaraBth
- LinkedIn details Mara Fenwick
- Mobile phone number 07812 459302
- Mission statement: To create a learning network that ensures that schools receive first class training that is excellent value for money.
Nice to have
- N/a
Should not have
- Twee educational images

```html
<!DOCTYPE html>
<html lang="en">
<head>
<meta charset="utf-8">
<title>Bright Tutor Hub – Business Card</title>
<link href="https://fonts.googleapis.com/css2?family=Montserrat:wght@700&family=Quicksand:wght@400;500&display=swap" rel="stylesheet">
<style>
  :root {
    --backdrop: #1a1a1a;
    --card: #161616;
    --card-edge: #3a3a3a;
    --silver: #c8c8c8;
    --silver-soft: #9a9a9a;
    --ink-muted: #8a8a8a;
  }
  * { box-sizing: border-box; margin: 0; padding: 0; }
  html, body {
    width: 1200px; height: 900px; overflow: hidden;
    background: var(--backdrop);
  }
  .canvas {
    width: 1200px; height: 900px;
    display: flex; flex-direction: column;
    align-items: center; justify-content: center; gap: 60px;
  }
  .card {
    width: 600px; height: 345px;
    background: linear-gradient(160deg, #202020 0%, var(--card) 60%, #111 100%);
    border-radius: 22px;
    border: 1px solid var(--card-edge);
    position: relative;
    font-family: 'Quicksand', sans-serif;
    color: var(--ink-muted);
  }

  /* Brand side */
  .card--brand {
    display: flex; flex-direction: column;
    align-items: center; justify-content: center;
  }
  .brand-mark {
    display: flex; align-items: center; gap: 14px;
  }
  .brand-mark__dot {
    width: 26px; height: 26px; border-radius: 50%;
    background: var(--silver);
  }
  .brand-mark__name {
    font-family: 'Montserrat', sans-serif;
    font-weight: 700;
    font-size: 38px;
    letter-spacing: 0.5px;
    color: var(--silver);
    text-transform: uppercase;
  }
  .mission {
    margin-top: 34px;
    width: 440px;
    text-align: center;
    font-size: 15px;
    line-height: 1.45;
    color: var(--ink-muted);
  }

  /* Contact side */
  .card--contact { padding: 46px 48px 0; }
  .person { text-align: center; }
  .person__name {
    font-family: 'Montserrat', sans-serif;
    font-weight: 700;
    font-size: 38px;
    color: var(--silver);
    text-transform: uppercase;
    letter-spacing: 0.5px;
  }
  .person__title {
    margin-top: 4px;
    font-size: 15px;
    color: var(--ink-muted);
  }
  .person__rule {
    width: 90px; height: 2px;
    background: var(--silver-soft);
    margin: 22px auto 0;
  }
  .contacts {
    position: absolute; left: 48px; right: 48px; bottom: 40px;
    display: flex; justify-content: space-between; align-items: flex-end;
  }
  .contacts__col { display: flex; flex-direction: column; gap: 10px; }
  .contact {
    display: flex; align-items: center; gap: 10px;
    font-size: 15px; color: var(--ink-muted);
  }
  .contact svg { width: 14px; height: 14px; flex: none; }
  .icon-stroke { fill: none; stroke: var(--ink-muted); stroke-width: 1.5; }
  .icon-fill { fill: var(--ink-muted); }
</style>
</head>
<body>
<main class="canvas">

  <section class="card card--brand" aria-label="Card front">
    <div class="brand-mark">
      <span class="brand-mark__dot"></span>
      <span class="brand-mark__name">Bright Tutor Hub</span>
    </div>
    <p class="mission">To create a learning network that ensures that schools receive first class training that is excellent value for money</p>
  </section>

  <section class="card card--contact" aria-label="Card back">
    <div class="person">
      <h1 class="person__name">Mara Fenwick</h1>
      <p class="person__title">Chief Executive Office</p>
      <div class="person__rule"></div>
    </div>

    <div class="contacts">
      <div class="contacts__col">
        <p class="contact">
          <svg viewBox="0 0 14 14"><circle class="icon-fill" cx="7" cy="7" r="6"/></svg>
          @MaraBth
        </p>
        <p class="contact">
          <svg viewBox="0 0 14 14"><rect class="icon-stroke" x="1" y="3" width="12" height="8"/><path class="icon-stroke" d="M1 3 L7 8 L13 3"/></svg>
          mara@brighttutorhub.co.uk
        </p>
      </div>
      <div class="contacts__col">
        <p class="contact">
          <svg viewBox="0 0 14 14"><rect class="icon-stroke" x="3.5" y="1" width="7" height="12" rx="1.2"/><line class="icon-stroke" x1="6" y1="11" x2="8" y2="11"/></svg>
          07812 459302
        </p>
        <p class="contact">
          <svg viewBox="0 0 14 14"><circle class="icon-stroke" cx="7" cy="7" r="6"/><ellipse class="icon-stroke" cx="7" cy="7" rx="2.6" ry="6"/><line class="icon-stroke" x1="1" y1="7" x2="13" y2="7"/></svg>
          www.brighttutorhub.co.uk
        </p>
        <p class="contact">
          <svg viewBox="0 0 14 14"><rect class="icon-fill" x="1" y="1" width="12" height="12" rx="1.5"/></svg>
          Mara Fenwick
        </p>
      </div>
    </div>
  </section>

</main>
</body>
</html>
```